Dribblecake Bites
2 x business cards, letter head, with complements and envelopes
Dribblecake Bites - Food
Creative Brief
Bright & Fun-filled
Percy Lantern
Managing Director
NA
Percy.Lantern@dribblecakebites.com.au
www.dribblecakebites.com.au
card 2 Teodor Blum Business Manager 0417583926 Teodorblum@quillnet.com www.dribblecakebites.com.au
logo ect

```html
<!DOCTYPE html>
<html lang="en">
<head>
<meta charset="utf-8">
<title>Dribblecake Bites – Business Card</title>
<link rel="stylesheet" href="https://fonts.googleapis.com/css2?family=Source+Sans+3:wght@400;600;700;800&family=Tinos&display=swap">
<style>
  :root {
    --backdrop: #3a3a3a;
    --card: #ffffff;
    --brown: #5b2a14;
    --brown-deep: #4a2010;
    --orange: #c8641e;
    --stripe: #e8d9cc;
    --text-muted: #3d3d3d;
    --rule: #b9b9b9;
  }
  * { margin: 0; padding: 0; box-sizing: border-box; }
  html, body { width: 1200px; height: 780px; overflow: hidden; }
  body {
    background: var(--backdrop);
    display: flex;
    align-items: center;
    justify-content: center;
    font-family: "Source Sans 3", sans-serif;
  }
  .business-card {
    position: relative;
    width: 900px;
    height: 540px;
    background: var(--card);
    border-radius: 36px;
    overflow: hidden;
  }
  .brand {
    position: absolute;
    left: 48px;
    top: 104px;
  }
  .brand-name {
    display: flex;
    align-items: center;
    gap: 14px;
    font-weight: 800;
    font-size: 76px;
    line-height: 1;
    color: var(--brown);
    letter-spacing: -1px;
  }
  .brand-dot {
    width: 26px;
    height: 26px;
    border-radius: 50%;
    background: var(--orange);
  }
  .person {
    position: absolute;
    left: 92px;
    top: 246px;
    text-align: right;
    width: 210px;
  }
  .person-name {
    font-weight: 700;
    font-size: 30px;
    color: var(--brown);
    line-height: 1.15;
  }
  .person-title {
    font-weight: 700;
    font-size: 24px;
    color: var(--orange);
  }
  .divider {
    position: absolute;
    left: 322px;
    top: 226px;
    width: 2px;
    height: 110px;
    background: var(--rule);
  }
  .contacts {
    position: absolute;
    left: 338px;
    top: 222px;
    list-style: none;
    font-family: "Tinos", serif;
    font-size: 21px;
    color: var(--text-muted);
  }
  .contacts li {
    display: flex;
    align-items: center;
    gap: 10px;
    height: 36px;
  }
  .contacts svg { width: 18px; height: 18px; flex: none; }
  .card-waves {
    position: absolute;
    left: 0;
    bottom: 0;
    width: 900px;
    height: 540px;
  }
</style>
</head>
<body>
  <div class="business-card">
    <svg class="card-waves" viewBox="0 0 900 540" aria-hidden="true">
      <path d="M0 395 C 230 470, 520 330, 900 350 L900 372 C 540 356, 250 490, 0 418 Z" fill="var(--stripe)"/>
      <path d="M0 430 C 240 500, 540 372, 900 385 L900 540 L0 540 Z" fill="var(--brown)"/>
      <path d="M0 430 C 240 500, 540 372, 900 385 L900 398 C 540 386, 250 514, 0 446 Z" fill="var(--orange)"/>
      <path d="M0 470 C 260 540, 560 420, 900 440 L900 540 L0 540 Z" fill="var(--brown-deep)"/>
    </svg>

    <div class="brand">
      <div class="brand-name"><span class="brand-dot"></span>Dribblecake Bites</div>
    </div>

    <div class="person">
      <div class="person-name">Percy Lantern</div>
      <div class="person-title">Managing Director</div>
    </div>

    <div class="divider"></div>

    <ul class="contacts">
      <li>
        <svg viewBox="0 0 24 24"><path d="M6.6 10.8a15 15 0 0 0 6.6 6.6l2.2-2.2a1 1 0 0 1 1-.25 11.4 11.4 0 0 0 3.6.57 1 1 0 0 1 1 1V20a1 1 0 0 1-1 1A17 17 0 0 1 3 4a1 1 0 0 1 1-1h3.5a1 1 0 0 1 1 1c0 1.250.2 2.450.57 3.570a1 1 0 0 1-.25 1z" fill="var(--brown)"/></svg>
        0431862057
      </li>
      <li>
        <svg viewBox="0 0 24 24"><circle cx="12" cy="12" r="10" fill="var(--brown)"/><circle cx="12" cy="12" r="4" fill="none" stroke="#fff" stroke-width="2"/></svg>
        Percy.Lantern@dribblecakebites.com.au
      </li>
      <li>
        <svg viewBox="0 0 24 24"><circle cx="12" cy="12" r="10" fill="var(--brown)"/><path d="M2 12h20M12 2c3 3 3 17 0 20M12 2c-3 3-3 17 0 20" fill="none" stroke="#fff" stroke-width="1.5"/></svg>
        www.dribblecakebites.com.au
      </li>
    </ul>
  </div>
</body>
</html>
```